Training Business needs brochure design for an employee questionnaire

We need an employee questionnaire to be in print. It needs to look more like an 8.5 x 11 inch brochure. It is for a training activity where people read questions about themselves, check the answer that is most like them and then figure out their scores (that's in the word doc). The score sheet will be a separate sheet, but needs a front and back designed (that's the ppt - SLIDES 2 and 3 attached here). For the score sheet I am not tied to putting in the arrow heads. Throughout, I would like to see an adventurous corporate theme that incorporates some of the Hollywood archery movies in the graphics--nothing like gimmick stock photo--but better graphics showing strength, insight and a mature warrior with a bow.
Updates

The images in this project should be more masculine than feminine. It is a leadership program, so I do not want cheesy pictures of girls with bows. It is a high-end corporate business leader training program and the design should be sophisticated but masculine. Most of the trainees will not related to a lot of the inexpensive images on the inexpensive stock photo sites. I also do not want blocks of photos and huge blocks of color, especially the gold. Gold should be an accent, please, not the overwhelming color on the page. The assessment of leaders should be what this portrays and communicates. Thanks! Added Wednesday, February 18, 2015

Reason: Designs submitted to this date do not look like executive leadership material - they look like 1990's mass market training brochures. My material will hit the trash with old designs.

Target Market(s)

Company employees learning to be team and business leaders, ages 25-35

Industry/Entity Type

Training

Colors
fece3e

Requirements
Must have
• Business leadership is the main theme of this communication. It is masculine, corporate sophistication, business. The color should be an accent, not an overwhelming piece of the message. Feeling of contemporary business and futuristic archery / fantasy like modern archery films in pop culture is the theme but the questionnaire and leadership development is the focus. Sample images are now provided for inspiration. If you use them, please crop or photoshop covering on the females so that they are portrayed with full clothing. People must be able to clearly read and respond to each question using the 1-5 ranking scale. People must be able to read and consider who they are, how they answer the questions, how they fill out the forms. ALSO...Must have a separate profile/score sheet where the score is on 1 side and the profile graphic is on the back. All are 8.5x11 inches. Must have company logo, copyright and address in there somewhere, but not a full page. THIS IS A MULTI PAGE PROJECT
Nice to have
• Creative use of white space. Very easy to read t.he instructions, the questions, and figure out how to select the answers.
Should not have
• Clutter or heavy color saturation

```html
<!DOCTYPE html>
<html lang="en">
<head>
<meta charset="utf-8">
<title>The Way of the Ancient Archer — Front Line Leadership Program</title>
<link rel="stylesheet" href="https://fonts.googleapis.com/css2?family=Open+Sans:wght@300;400;700&display=swap">
<style>
  :root {
    --gold: #fcc93a;
    --ink: #3f454c;
    --heading-ink: #2f363d;
    --paper: #ffffff;
    --frame-light: #f6b58a;
    --frame-orange: #ee8a3c;
    --frame-red: #e5392b;
    --frame-amber: #e6a233;
  }
  * { margin: 0; padding: 0; box-sizing: border-box; }
  html, body {
    width: 927px;
    height: 1200px;
    overflow: hidden;
  }
  body {
    font-family: "Open Sans", Arial, sans-serif;
    color: var(--ink);
    position: relative;
  }
  .frame-pattern {
    position: absolute;
    inset: 0;
    background:
      radial-gradient(ellipse at 20% 5%, rgba(250, 214, 180, 0.9), transparent 45%),
      radial-gradient(ellipse at 100% 40%, var(--frame-red), transparent 60%),
      radial-gradient(ellipse at 5% 60%, rgba(232, 180, 90, 0.9), transparent 45%),
      radial-gradient(ellipse at 60% 100%, var(--frame-amber), transparent 55%),
      linear-gradient(135deg, var(--frame-light) 0%, var(--frame-orange) 45%, var(--frame-red) 100%);
  }
  .page {
    position: absolute;
    left: 43px;
    top: 43px;
    width: 841px;
    height: 1114px;
    background: var(--paper);
  }
  .masthead {
    position: absolute;
    left: 42px;
    top: 232px;
    width: 757px;
  }
  .masthead__title {
    color: var(--gold);
    font-weight: 700;
    font-size: 35px;
    line-height: 36px;
  }
  .masthead__rule {
    position: absolute;
    left: 400px;
    top: 68px;
    width: 357px;
    height: 2px;
    background: var(--gold);
  }
  .masthead__subtitle {
    color: var(--gold);
    font-weight: 300;
    font-size: 19.5px;
    line-height: 26px;
  }
  .column {
    position: absolute;
    top: 358px;
    font-weight: 300;
    font-size: 17px;
    line-height: 24.7px;
  }
  .column p + p { margin-top: 24.7px; }
  .column--intro { left: 43px; width: 375px; }
  .column--questionnaire { left: 442px; width: 372px; }
  .column__heading {
    font-weight: 700;
    font-size: 17px;
    line-height: 24.7px;
    color: var(--heading-ink);
    margin-bottom: 24.7px;
  }
</style>
</head>
<body>
  <div class="frame-pattern" role="img" aria-label="Low-poly faceted background in warm orange, red and amber tones"></div>

  <main class="page">
    <header class="masthead">
      <h1 class="masthead__title">The Way<br>of the Ancient Archer</h1>
      <span class="masthead__rule"></span>
      <p class="masthead__subtitle">Front Line Leadership Program</p>
    </header>

    <section class="column column--intro">
      <p>Business Leaders are much like ancient archers who were the first to step to the line of battle. Confident, well-prepared, fearless and great in strength, vision and perseverance—these warriors led the way into battle.</p>
      <p>The leaders of ancient archers were the ones who set these courageous, trained, brave warriors to the front-line. The way of the ancient archer is one of strong performance, agile, dependable, and cooperative. They were power houses. Their performance was based on a solid foundation of knowledge and teamwork and steady nerves. They had control, visionary insight and discipline to execute commands that supported the ranks of warriors behind them.</p>
      <p>The way of the ancient archer is a lost way of life. They were warriors who won or lost kingdoms. They practiced their armed martial arts with precision. They practiced with such passion that they changed the bones in their bodies. Archeologists say they can always tell who was an archer. For the archer's reach was long and powerful and dangerous to the competition. It's very much like modern business.</p>
    </section>

    <section class="column column--questionnaire">
      <h2 class="column__heading">Questionnaire</h2>
      <p>This questionnaire is designed to help front-line managers to correlate the qualities of timeless traits of competence, courage, speed, strength, awareness and insight from the core of archery over the history of mankind, to develop awareness and insight into developing their own style of leadership.</p>
    </section>
  </main>
</body>
</html>
```